Letterhead for SaaS

Design a letterhead that aligns with our new business card, using our logo and color scheme and text defined in the Branding Guide to ensure consistency. Consider incorporating a subtle watermark for added elegance. The layout should reflect the card's style, creating a cohesive look across our stationery.

```html
<!DOCTYPE html>
<html lang="en">
<head>
<meta charset="utf-8">
<title>Norvane Stationery</title>
<link rel="stylesheet" href="https://fonts.googleapis.com/css2?family=Ubuntu:wght@500;700&family=Rubik:wght@700&family=Arimo:wght@400&display=swap">
<style>
  :root {
    --navy: #131a2a;
    --navy-soft: #1c2437;
    --sky: #3ab4e6;
    --paper: #ffffff;
    --stage: #3a3d40;
    --watermark: #e6e6e6;
    --label: #ffffff;
  }
  * { box-sizing: border-box; margin: 0; padding: 0; }
  html, body { width: 1200px; height: 900px; overflow: hidden; }
  body { background: var(--stage); position: relative; font-family: "Arimo", Arial, sans-serif; }

  .piece-label {
    position: absolute;
    font-family: "Ubuntu", Arial, sans-serif;
    font-weight: 700;
    font-size: 19px;
    color: var(--label);
    letter-spacing: 0.2px;
  }
  .sheet { position: absolute; background: var(--paper); overflow: hidden; }
  .brand-name {
    font-family: "Rubik", Arial, sans-serif;
    font-weight: 700;
    color: var(--navy);
    letter-spacing: 0.3px;
  }

  /* Letterhead */
  .letterhead { left: 615px; top: 139px; width: 533px; height: 689px; }
  .letterhead__band {
    position: absolute; left: 0; top: 0; width: 100%; height: 73px;
    background: linear-gradient(100deg, var(--navy) 0%, var(--navy-soft) 50%, var(--navy) 100%);
  }
  .letterhead__contacts {
    position: absolute; left: 18px; top: 33px;
    color: #fff; font-size: 10px; line-height: 16px;
  }
  .contact-row { display: flex; align-items: center; gap: 4px; }
  .contact-row svg { width: 11px; height: 11px; flex: none; }
  .contact-row .gap { width: 6px; }
  .letterhead__brand {
    position: absolute; right: 10px; top: 88px; font-size: 14px;
  }
  .letterhead__watermark {
    position: absolute; left: 0; top: 82px; width: 325px; height: 602px;
    background: linear-gradient(160deg, var(--watermark) 0%, #f1f1f1 70%, #fafafa 100%);
  }

  /* Envelope front */
  .envelope-front { left: 77px; top: 311px; width: 455px; height: 197px; }
  .envelope-front__brand { position: absolute; left: 19px; top: 51px; font-size: 8px; }
  .envelope-front__band {
    position: absolute; left: 0; top: 137px; width: 100%; height: 51px;
    background: linear-gradient(100deg, var(--navy) 0%, var(--navy-soft) 50%, var(--navy) 100%);
  }
  .envelope-front__address {
    position: absolute; left: 14px; top: 19px; color: #fff; font-size: 7.5px; line-height: 10px;
  }

  /* Envelope back */
  .envelope-back { left: 104px; top: 601px; width: 456px; height: 198px; }
  .envelope-back__flap { position: absolute; left: 0; top: 0; width: 456px; height: 74px; }
  .envelope-back__brand {
    position: absolute; left: 0; width: 100%; top: 38px; text-align: center;
    font-size: 11px; color: var(--sky);
  }
</style>
</head>
<body>

  <h2 class="piece-label" style="left:615px; top:92px;">Letterhead_3</h2>
  <section class="sheet letterhead">
    <div class="letterhead__band">
      <div class="letterhead__contacts">
        <div class="contact-row">
          <svg viewBox="0 0 12 12"><path fill="#3ab4e6" d="M1 4c0-2 2-3 5-3s5 1 5 3l-2 1-1-2H4L3 5zM3 6h6l1 5H2z"/></svg>
          <span>(555) 014-2290</span>
        </div>
        <div class="contact-row">
          <svg viewBox="0 0 12 12"><rect x="1" y="2.5" width="10" height="7" fill="#3ab4e6"/><path d="M1 2.5l5 4 5-4" stroke="#131a2a" stroke-width="1" fill="none"/></svg>
          <span>hello@norvane.io</span>
          <span class="gap"></span>
          <svg viewBox="0 0 12 12"><circle cx="6" cy="6" r="5" fill="#3ab4e6"/><path d="M3 3c2 1 2 3 4 3s1 3 0 4M8 2c0 1 1 2 2 2" stroke="#fff" stroke-width="1" fill="none"/></svg>
          <span>www.norvane.io</span>
        </div>
      </div>
    </div>
    <div class="brand-name letterhead__brand">NORVANE</div>
    <div class="letterhead__watermark" role="img" aria-label="Faint low-poly line-art watermark in light grey"></div>
  </section>

  <h2 class="piece-label" style="left:77px; top:265px;">Envelope Front_3</h2>
  <section class="sheet envelope-front">
    <div class="brand-name envelope-front__brand">NORVANE</div>
    <div class="envelope-front__band">
      <div class="envelope-front__address">Millbrook<br>Oregon 97120, US</div>
    </div>
  </section>

  <h2 class="piece-label" style="left:104px; top:555px;">Envelope Back_3</h2>
  <section class="sheet envelope-back">
    <svg class="envelope-back__flap" viewBox="0 0 456 74" aria-hidden="true">
      <path fill="#131a2a" d="M0 0H456C448 20 440 38 420 43C370 52 300 60 228 72C156 60 86 52 36 43C16 38 8 20 0 0Z"/>
    </svg>
    <div class="brand-name envelope-back__brand">NORVANE</div>
  </section>

</body>
</html>
```